Für ein Ebook mit dem Titel 'Lichtung - Atemzug für das Herz' mit dem Autorennamen Corinna Wendel benötige ich ein ansprechendes Cover.
Es sollte nicht zu bunt sein. Eher sinnlich und beruhigend. Erdtöne

```html
<!DOCTYPE html>
<html lang="de">
<head>
<meta charset="utf-8">
<title>Lichtung – Atemzug für das Herz</title>
<link rel="stylesheet" href="https://fonts.googleapis.com/css2?family=Josefin+Slab:wght@300;400&display=swap">
<style>
  :root {
    --paper: #f2e9e1;
    --ink: #5c5047;
    --sand: #cfb79f;
    --umber: #5c5047;
    --clay: #c29f80;
    --bark: #654f3d;
  }
  html, body {
    margin: 0;
    padding: 0;
    overflow: hidden;
    background: var(--paper);
  }
  .cover {
    position: relative;
    width: 752px;
    height: 1200px;
    overflow: hidden;
    background: var(--paper);
    font-family: "Josefin Slab", Georgia, serif;
    color: var(--ink);
  }
  .cover__shapes {
    position: absolute;
    inset: 0;
    width: 752px;
    height: 1200px;
  }
  .cover__title {
    position: absolute;
    top: 150px;
    left: 0;
    width: 752px;
    margin: 0;
    text-align: center;
    font-weight: 400;
    font-size: 82px;
    line-height: 106px;
    letter-spacing: 1px;
  }
  .cover__title span { display: block; }
  .cover__author {
    position: absolute;
    top: 650px;
    left: 0;
    width: 752px;
    margin: 0;
    text-align: center;
    font-weight: 400;
    font-size: 52px;
    letter-spacing: 0.5px;
  }
  .cover__figure {
    position: absolute;
    left: 238px;
    top: 807px;
    width: 277px;
    height: 393px;
    border-radius: 138px 138px 60px 60px;
    background: linear-gradient(180deg, var(--bark) 0%, var(--clay) 60%, var(--bark) 100%);
    opacity: 0.85;
  }
</style>
</head>
<body>
  <main class="cover">
    <svg class="cover__shapes" viewBox="0 0 1057 1687" preserveAspectRatio="none" aria-hidden="true">
      <path fill="var(--sand)" d="M0,895 C80,915 140,940 190,970 C280,1050 360,1160 350,1240 C340,1320 290,1360 240,1395 L0,1420 Z"/>
      <path fill="var(--umber)" d="M0,1420 C40,1420 80,1430 100,1400 C130,1340 120,1250 170,1250 C220,1250 250,1330 245,1400 C240,1500 180,1580 170,1630 L175,1687 L0,1687 Z"/>
      <path fill="var(--sand)" d="M1057,1245 C1000,1250 980,1300 970,1360 C955,1440 900,1470 820,1520 C760,1560 730,1620 730,1687 L1057,1687 Z"/>
    </svg>

    <h1 class="cover__title">
      <span>Lichtung</span>
      <span>–</span>
      <span>Atemzug für das</span>
      <span>Herz</span>
    </h1>

    <p class="cover__author">Corinna Wendel</p>

    <div class="cover__figure" role="img" aria-label="Illustration einer meditierenden Person im Schneidersitz in Erdtönen"></div>
  </main>
</body>
</html>
```